Altamira Business Card Design

The name of the business is Ruben Altamira, CPA LLC
The service that we offer is Accounting, Tax & Consulting Services. I need it to have the following items:
Ruben Altamira, Principal
Phone Number
Email Address
Physical Address

I have attached the company logo, one in black and one in white. Please provide a design in black background and the other in white background. Please include "Accounting, Tax & Consulting Services". I want the business card to be clean and very professional.

```html
<!DOCTYPE html>
<html lang="en">
<head>
<meta charset="utf-8">
<title>Ruben Altamira, CPA LLC — Business Card</title>
<link href="https://fonts.googleapis.com/css2?family=Mulish:wght@400;500;600&display=swap" rel="stylesheet">
<style>
  :root {
    --page: #2a2a2b;
    --card-light: #ebebec;
    --card-dark: #3b3c3e;
    --red: #a01c22;
    --ink: #3d3e40;
    --grey: #7b7c7f;
    --white: #ffffff;
  }
  * { margin: 0; padding: 0; box-sizing: border-box; }
  html, body { width: 1200px; height: 1200px; overflow: hidden; }
  body {
    background: var(--page);
    font-family: "Mulish", Arial, sans-serif;
    position: relative;
  }
  .card {
    position: absolute;
    left: 229px;
    width: 742px;
    height: 429px;
    overflow: hidden;
  }

  /* Front */
  .card-front { top: 172px; background: var(--card-light); }
  .front-brand { position: absolute; left: 71px; top: 58px; }
  .front-brand .firm {
    font-size: 21px; font-weight: 500; color: var(--ink);
    letter-spacing: 0.3px; text-transform: uppercase; white-space: nowrap;
  }
  .front-brand .designation {
    font-size: 13px; font-weight: 500; color: var(--grey);
    letter-spacing: 1.6px; text-transform: uppercase; margin-top: 2px;
  }
  .front-mark {
    position: absolute; left: 140px; top: 218px;
    font-size: 26px; font-weight: 600; color: var(--ink);
    letter-spacing: 2px; text-transform: uppercase;
  }
  .person { position: absolute; left: 456px; top: 50px; }
  .person .name {
    font-size: 24px; font-weight: 500; color: var(--ink);
    text-transform: uppercase; letter-spacing: 0.4px;
  }
  .person .name .first { color: var(--red); }
  .person .role { font-size: 16px; color: var(--ink); margin-top: 2px; }
  .person-rule {
    position: absolute; left: 456px; right: 0; top: 122px;
    height: 1.5px; background: var(--red);
  }
  .address {
    position: absolute; left: 446px; top: 206px;
    font-size: 16px; line-height: 25px; color: var(--red);
  }
  .contact-bar {
    position: absolute; left: 446px; top: 264px; bottom: 0;
    width: 31px; background: var(--red);
  }
  .contact-list {
    position: absolute; left: 446px; top: 268px; list-style: none;
  }
  .contact-list li {
    display: flex; align-items: center; height: 25px;
    font-size: 16px; color: var(--ink);
  }
  .contact-list svg { width: 31px; height: 14px; flex: none; margin-right: 10px; }

  /* Back */
  .card-back { top: 646px; height: 428px; background: var(--card-dark); }
  .back-brand {
    position: absolute; left: 137px; top: 162px;
    display: flex; align-items: center; gap: 22px;
  }
  .back-brand .square { width: 46px; height: 46px; background: var(--white); flex: none; }
  .back-brand .firm {
    font-size: 28px; font-weight: 500; color: var(--white);
    text-transform: uppercase; letter-spacing: 0.3px; white-space: nowrap; line-height: 1.1;
  }
  .back-brand .designation {
    font-size: 19px; font-weight: 500; color: var(--white);
    text-transform: uppercase; letter-spacing: 1.8px; margin-top: 4px;
  }
  .service-band {
    position: absolute; left: 0; right: 0; bottom: 0; height: 53px; background: var(--red);
  }
  .service-tab {
    position: absolute; left: 116px; width: 492px; bottom: 0; height: 84px;
    background: var(--red); border-radius: 12px 12px 0 0;
  }
  .service-tab span {
    position: absolute; left: 21px; top: 12px;
    font-size: 24px; color: var(--white); white-space: nowrap;
  }
</style>
</head>
<body>

  <section class="card card-front" aria-label="Front of business card">
    <div class="front-brand">
      <div class="firm">Ruben Altamira, CPA LLC</div>
      <div class="designation">Certified Public Accountant</div>
    </div>

    <div class="front-mark">Altamira</div>

    <div class="person">
      <div class="name"><span class="first">Ruben</span> Altamira</div>
      <div class="role">Principal</div>
    </div>
    <div class="person-rule"></div>

    <address class="address" style="font-style:normal">
      Po box 2870 linden<br>calgaro, ab tk-4r7
    </address>

    <div class="contact-bar"></div>
    <ul class="contact-list">
      <li>
        <svg viewBox="0 0 31 14" aria-hidden="true"><path fill="#fff" d="M11 2.5c.6-.6 1.3-.5 1.7.1l1.2 1.7c.3.5.2 1-.2 1.4l-.8.7c.5 1.1 1.4 2 2.5 2.5l.7-.8c.4-.4.9-.5 1.4-.2l1.7 1.2c.6.4.7 1.1.1 1.7l-.8.8c-.9.9-2.5.6-4.4-.7-1.5-1-2.9-2.4-3.9-3.9C9 5.2 8.7 3.6 9.6 2.7z"/></svg>
        415 (0) 552 804 617
      </li>
      <li>
        <svg viewBox="0 0 31 14" aria-hidden="true"><rect x="10" y="3.5" width="11" height="7.5" fill="#fff"/><path d="M10 3.5l5.5 4 5.5-4" fill="none" stroke="#a01c22" stroke-width="1"/></svg>
        hello(@)altamiracpa.co
      </li>
      <li>
        <svg viewBox="0 0 31 14" aria-hidden="true"><circle cx="15.5" cy="7" r="5.5" fill="#fff"/><path d="M12.5 5.5c1 .3 1.5 1 1.2 2s.8 1.5 1.5 2.8M17 2.5c-.6 1-.2 2 .8 2.3s1.6 1 1.6 2" fill="none" stroke="#a01c22" stroke-width="1"/></svg>
        www.altamiracpa.co
      </li>
    </ul>
  </section>

  <section class="card card-back" aria-label="Back of business card">
    <div class="back-brand">
      <div class="square"></div>
      <div>
        <div class="firm">Ruben Altamira, CPA LLC</div>
        <div class="designation">Certified Public Accountant</div>
      </div>
    </div>

    <div class="service-band"></div>
    <div class="service-tab"><span>Accounting, Tax &amp; Consulting Services</span></div>
  </section>

</body>
</html>
```